Stationary Design needed for Physical Therapy and Wellness Center

Letterhead, Envelopes, Business Cards (x2) needed. We are a studio specializing in helping our clients improve mobility, fitness, and recover from injury. We use the Velantric method and need to adhere to their trademark restrictions.
Updates

Target Market(s)

Potential Clients: active people...many from dance or athletic backgrounds.

Industry/Entity Type

Health And Wellness

Font styles to use
Sans Serif
Other font styles liked:
• Times New Roman for the word Velantric.

Colors
00a990
33b8a4
86cfc6
0393ce
33a6d7
85cae6

Requirements
Must have
• Attention to Velantric trademark guidelines (Times New Roman font, Bold type, use of registered trademark symbol). Examples of current stationary can be provided as an example.
• Concept of movement, flow.

```html
<!DOCTYPE html>
<html lang="en">
<head>
<meta charset="utf-8">
<title>flowline stationery</title>
<link rel="stylesheet" href="https://fonts.googleapis.com/css2?family=Questrial&family=Tinos:wght@400;700&display=swap">
<style>
:root{
  --teal:#00a990;
  --teal-mid:#33b8a4;
  --teal-soft:#86cfc6;
  --teal-deep:#06867c;
  --blue:#0393ce;
  --blue-mid:#33a6d7;
  --blue-soft:#85cae6;
  --navy:#0b3f8f;
  --ink:#1f1f1f;
  --paper:#ffffff;
  --backdrop:#d6d7d9;
}
*{margin:0;padding:0;box-sizing:border-box}
html,body{width:1200px;height:751px;overflow:hidden}
body{background:var(--backdrop);position:relative;font-family:"Tinos","Times New Roman",serif}
.sheet{position:absolute;background:var(--paper);overflow:hidden;box-shadow:0 4px 14px rgba(0,0,0,.18)}
.sheet>svg.art{position:absolute;inset:0}
.abs{position:absolute}
.brand{font-family:"Questrial",sans-serif;font-weight:400;white-space:nowrap;letter-spacing:.2px}
.icon{width:1em;height:1em;vertical-align:-.12em;margin-right:.45em}
.contact{list-style:none;font-weight:700;white-space:nowrap}

/* letterhead */
.letterhead{left:68px;top:112px;width:385px;height:543px}
.letterhead .brand{left:30px;top:46px;font-size:22px;color:var(--paper)}
.letterhead .sender{left:281px;top:54px;color:var(--ink)}
.letterhead .sender-name{font-size:7.3px;font-weight:700;margin-bottom:2px;white-space:nowrap}
.letterhead .contact{font-size:6.6px;line-height:9.2px;color:var(--ink)}
.letterhead .footer-web{right:3px;bottom:4px;font-size:10.5px;font-weight:700;color:var(--paper)}

/* business cards */
.card{top:134px;width:281px;height:179px}
.card-front{left:556px}
.card-front .brand{left:0;right:0;top:72px;text-align:center;font-size:28px;color:var(--teal-deep)}
.card-back{left:855px}
.card-back .brand{left:5px;top:28px;font-size:10px;color:var(--paper)}
.card-back .details{left:82px;top:38px;color:var(--teal)}
.card-back .holder{font-size:10px;font-weight:700;color:var(--blue);white-space:nowrap;padding-bottom:2px;border-bottom:1px solid var(--blue-soft);display:inline-block}
.card-back .titles{list-style:none;font-size:7.6px;font-weight:700;line-height:10.3px;margin-top:6px;white-space:nowrap}
.card-back .contact{font-size:8.6px;line-height:11.4px;margin-top:9px;margin-left:5px}
.mark{font-family:"Tinos","Times New Roman",serif;font-weight:700}

/* envelope */
.envelope{left:590px;top:400px;width:554px;height:241px}
.envelope .brand{left:18px;top:50px;font-size:17px;color:var(--teal-deep)}
.envelope .to{left:173px;top:84px;font-family:"Questrial",sans-serif;font-size:11px;font-weight:700;color:var(--ink)}
.envelope .address-line{left:200px;width:310px;height:1px;background:#555}
.envelope .contact{left:13px;top:121px;font-size:9.2px;line-height:14.5px;color:var(--ink)}
</style>
</head>
<body>

<svg width="0" height="0" style="position:absolute" aria-hidden="true">
  <symbol id="i-phone" viewBox="0 0 16 16"><circle cx="8" cy="8" r="6.6" fill="none" stroke="currentColor" stroke-width="1.6"/><path d="M5.6 4.6l1.4-.3.8 2-1 .7a5 5 0 0 0 2.2 2.2l.7-1 2 .8-.3 1.4c-3.2.3-6.1-2.6-5.8-5.8z" fill="currentColor"/></symbol>
  <symbol id="i-mail" viewBox="0 0 16 16"><rect x="1" y="3.5" width="14" height="9" fill="currentColor"/><path d="M1 3.5l7 5 7-5" fill="none" stroke="#fff" stroke-width="1.2"/></symbol>
  <symbol id="i-web" viewBox="0 0 16 16"><circle cx="8" cy="8" r="6.8" fill="currentColor"/><path d="M4 5c2 0 2 2 4 2s1 3-1 3-2 2-2 3M10 3c0 2 2 2 3 4" fill="none" stroke="#fff" stroke-width="1.3"/></symbol>
</svg>

<!-- Letterhead -->
<section class="sheet letterhead" aria-label="Letterhead">
  <svg class="art" viewBox="0 0 385 543" aria-hidden="true">
    <path d="M0 0H385V10C330 8 272 36 222 58C160 84 90 88 0 72Z" fill="var(--blue)"/>
    <path d="M250 46C300 24 345 10 385 14V22C340 18 300 30 262 48Z" fill="var(--paper)"/>
    <path d="M180 66C250 40 320 26 385 36V40C320 32 260 46 200 68Z" fill="var(--blue-mid)"/>
    <path d="M0 50C60 74 130 86 200 70C260 55 320 34 385 38V42C320 40 262 60 210 80C140 104 60 100 0 76Z" fill="var(--teal-soft)"/>
    <path d="M0 488C60 518 150 524 230 500C300 478 345 460 385 484V543H0Z" fill="var(--blue)"/>
    <path d="M0 498C70 526 140 532 205 518C140 546 60 544 0 522Z" fill="var(--teal-soft)"/>
  </svg>
  <div class="abs brand">flowline</div>
  <div class="abs sender">
    <p class="sender-name">DANIEL HARLOW, MSPT, ATC</p>
    <ul class="contact">
      <li><svg class="icon"><use href="#i-phone"/></svg>555-014-2290</li>
      <li><svg class="icon"><use href="#i-mail"/></svg>Daniel@flowlinept.com</li>
      <li><svg class="icon"><use href="#i-web"/></svg>www.flowlinept.com</li>
    </ul>
  </div>
  <div class="abs footer-web">www.flowlinept.com</div>
</section>

<!-- Business card front -->
<section class="sheet card card-front" aria-label="Business card front">
  <svg class="art" viewBox="0 0 281 179" aria-hidden="true">
    <defs>
      <linearGradient id="g-front" x1="0" y1="0" x2="1" y2="1">
        <stop offset="0" stop-color="#16b4e6"/><stop offset=".5" stop-color="var(--blue)"/><stop offset="1" stop-color="var(--navy)"/>
      </linearGradient>
    </defs>
    <rect width="281" height="179" fill="url(#g-front)"/>
    <path d="M0 0H50C30 8 10 20 0 30Z" fill="var(--paper)"/>
    <path d="M230 0H281V10C265 5 250 2 230 0Z" fill="var(--teal-soft)"/>
    <ellipse cx="148" cy="92" rx="165" ry="82" fill="none" stroke="var(--teal)" stroke-width="5"/>
    <ellipse cx="145" cy="90" rx="160" ry="76" fill="var(--paper)"/>
  </svg>
  <div class="abs brand">flowline</div>
</section>

<!-- Business card back -->
<section class="sheet card card-back" aria-label="Business card back">
  <svg class="art" viewBox="0 0 281 179" aria-hidden="true">
    <defs>
      <linearGradient id="g-back" x1="0" y1="0" x2="0" y2="1">
        <stop offset="0" stop-color="var(--teal)"/><stop offset=".45" stop-color="var(--blue)"/><stop offset="1" stop-color="var(--teal)"/>
      </linearGradient>
    </defs>
    <path d="M0 0H153C100 16 66 44 60 85C55 125 64 158 80 179H0Z" fill="url(#g-back)"/>
    <path d="M118 0C80 22 52 55 40 110" fill="none" stroke="var(--navy)" stroke-width="3"/>
    <path d="M0 90C20 120 40 150 40 179H0Z" fill="var(--teal-deep)" opacity=".7"/>
  </svg>
  <div class="abs brand">flowline</div>
  <div class="abs details">
    <p class="holder">DANIEL HARLOW, MSPT, ATC</p>
    <ul class="titles">
      <li>Licensed Physical Therapist</li>
      <li>Certified Athletic Trainer</li>
      <li>Certified <span class="mark">VELANTRIC®</span> Instructor</li>
      <li>Figure Skating Coach</li>
    </ul>
    <ul class="contact">
      <li><svg class="icon" style="color:var(--ink)"><use href="#i-phone"/></svg>555-014-2290</li>
      <li><svg class="icon" style="color:var(--ink)"><use href="#i-mail"/></svg>Daniel@flowlinept.com</li>
      <li><svg class="icon" style="color:var(--ink)"><use href="#i-web"/></svg>www.flowlinept.com</li>
    </ul>
  </div>
</section>

<!-- Envelope -->
<section class="sheet envelope" aria-label="Envelope">
  <svg class="art" viewBox="0 0 554 241" aria-hidden="true">
    <path d="M300 0H554V24C470 36 380 28 300 0Z" fill="var(--teal-deep)"/>
    <path d="M318 0C380 22 440 32 520 30" fill="none" stroke="#2b2b2b" stroke-width="3"/>
    <path d="M350 0C400 18 460 26 554 22" fill="none" stroke="var(--paper)" stroke-width="3"/>
    <path d="M0 241V210C90 196 190 200 252 241Z" fill="var(--teal-deep)"/>
    <path d="M0 208C90 194 170 198 218 241" fill="none" stroke="var(--paper)" stroke-width="3"/>
    <path d="M90 200C150 200 195 215 230 241" fill="none" stroke="#2b2b2b" stroke-width="3"/>
  </svg>
  <div class="abs brand">flowline</div>
  <div class="abs to">To,</div>
  <div class="abs address-line" style="top:94px"></div>
  <div class="abs address-line" style="top:134px"></div>
  <ul class="abs contact">
    <li><svg class="icon"><use href="#i-phone"/></svg>555-014-2290</li>
    <li><svg class="icon"><use href="#i-mail"/></svg>Daniel@flowlinept.com</li>
    <li><svg class="icon"><use href="#i-web"/></svg>www.flowlinept.com</li>
  </ul>
</section>

</body>
</html>
```